Vantor 9 Skins

Hey I need 2 stickers made one for my vantor 9 Rower and one for my vantor 9 pulse tor.I have attached some images of the rower and pulse tor as well as some photos of the rower and ski with some stickers already done.And i have attached my logo so you can get a feel for how i would like it designed and the logos that need to be included.

Target Market(s)

TO BE STUCK ON THE MACHINES IN A GYM

The rowers will need to be reversable.

Font styles to use
Serif
Sans Serif
Other font styles liked:
• LATO

Colors
0392cd
33a6d7
85cae6
ffffff
0255a3
3176b5
cedeed
85acd3
e34197

```html
<!DOCTYPE html>
<html lang="en">
<head>
<meta charset="utf-8">
<title>Rower D1 – Machine Sticker</title>
<link rel="stylesheet" href="https://fonts.googleapis.com/css2?family=Open+Sans:wght@700&display=swap">
<style>
  :root {
    --ink: #262a5e;
    --frame: #2e3192;
    --blue-deep: #0392cd;
    --blue-mid: #33a6d7;
    --blue-soft: #85cae6;
    --blue-pale: #cedeed;
    --white: #ffffff;
  }
  html, body {
    margin: 0;
    padding: 0;
    width: 1200px;
    height: 680px;
    overflow: hidden;
    background: var(--white);
  }
  .sticker {
    position: relative;
    width: 1200px;
    height: 680px;
    background: var(--white);
    font-family: "Open Sans", sans-serif;
  }
  .wave-banner {
    position: absolute;
    left: 50px;
    top: 122px;
    width: 1072px;
    height: 134px;
    box-sizing: border-box;
    border: 2px solid var(--frame);
    overflow: hidden;
  }
  .wave-banner__art {
    position: absolute;
    inset: 0;
    background:
      linear-gradient(175deg, rgba(3,146,205,0.85) 0%, rgba(133,202,230,0.5) 30%, rgba(255,255,255,0) 55%),
      linear-gradient(90deg, var(--blue-mid) 0%, var(--blue-soft) 30%, var(--white) 55%, var(--blue-pale) 80%, var(--blue-deep) 100%);
  }
  .brand-mark {
    position: absolute;
    right: 14px;
    top: 50%;
    transform: translateY(-50%);
    width: 112px;
    height: 112px;
    display: flex;
    align-items: center;
    justify-content: center;
  }
  .brand-mark__ring {
    position: absolute;
    inset: 0;
  }
  .brand-mark__name {
    position: relative;
    font-size: 20px;
    font-weight: 700;
    letter-spacing: 0.14em;
    color: var(--ink);
    background: var(--white);
    padding: 0 4px;
  }
  .machine-title {
    position: absolute;
    left: 0;
    width: 1272px;
    top: 336px;
    margin: 0;
    text-align: center;
    font-size: 46px;
    font-weight: 700;
    letter-spacing: 0.48em;
    color: var(--ink);
  }
</style>
</head>
<body>
  <main class="sticker">
    <div class="wave-banner">
      <div class="wave-banner__art" role="img" aria-label="Flowing blue wave graphic with dotted halftone bands"></div>
      <div class="brand-mark">
        <svg class="brand-mark__ring" viewBox="0 0 112 112" aria-hidden="true">
          <circle cx="56" cy="56" r="54" fill="var(--white)" stroke="var(--ink)" stroke-width="2"/>
        </svg>
        <span class="brand-mark__name">KESTREL</span>
      </div>
    </div>
    <h1 class="machine-title">Rower D1</h1>
  </main>
</body>
</html>
```